If everything digital fails, here's what to do

Hi, I would like a poster / infographic of a list of practical actions people could take in case the internet stops working. I've put together a list of 8 areas, with the situation for each, and the mitigation actions folks can take - I need it presented in a clear and aesthetically pleasing way. I will send you the file with the full text so you can include it all

Target Market(s)

General population, but likely people who are safety conscious and want to protect themselves and learn more about what to do to be tech literate and prepared

Industry/Entity Type

Tech / Cyber / Public safety / Civic tech

Font styles to use
Sans Serif

Requirements
Must have
• It's a lot of text, so I think the important thing is to have it all in one poster, or in a series of similar pages
Nice to have
• I would like it to be a bit brooding, but also elicit competence and that some experts have thought about this and it will all be okay
Should not have
• I don't want it to look cartoonish, or cheap - less is more is sort of what I'm looking for

```html
<!DOCTYPE html>
<html lang="en">
<head>
<meta charset="utf-8">
<title>If Everything Digital Fails, Here's What To Do</title>
<link href="https://fonts.googleapis.com/css2?family=Montserrat:wght@600;700;800&family=Open+Sans:wght@400;600&display=swap" rel="stylesheet">
<style>
  :root{
    --backdrop:#d8dbdf;
    --paper:#eef0f3;
    --navy:#1f2c4c;
    --steel:#5b7ea2;
    --panel:#dde4ec;
    --alert:#e0585d;
    --ink:#3c4658;
    --muted:#7a8494;
    --white:#ffffff;
  }
  *{box-sizing:border-box;margin:0;padding:0}
  html,body{width:1200px;height:2224px;overflow:hidden;background:var(--backdrop)}
  .canvas{position:relative;width:1200px;height:2224px;background:var(--backdrop);font-family:"Open Sans",Arial,sans-serif;color:var(--ink)}
  .page{position:absolute;width:520px;height:700px;background:var(--paper);box-shadow:0 3px 10px rgba(20,30,50,.18);overflow:hidden}
  .page--cover{left:50px;top:30px}
  .page--comms{left:630px;top:30px}
  .page--banking{left:50px;top:770px}
  .page--info{left:630px;top:770px}
  .page--tech{left:50px;top:1510px}
  .page--closing{left:630px;top:1510px}

  .block{position:absolute}
  .section-head{display:flex;align-items:center;gap:12px;margin-bottom:12px}
  .hex{width:38px;height:42px;flex:none}
  .hex polygon{fill:var(--navy)}
  .hex path{fill:none;stroke:var(--white);stroke-width:2;stroke-linecap:round}
  .section-title{font-family:"Montserrat",Arial,sans-serif;font-weight:800;font-size:17px;letter-spacing:.04em;color:var(--navy)}
  .section-sub{font-size:11px;color:var(--muted);margin-top:2px}

  .item{display:flex;align-items:center;gap:10px;background:var(--panel);padding:9px 12px;margin-bottom:8px;font-size:11.5px;line-height:1.4}
  .item-icon{width:24px;height:24px;flex:none}
  .item-icon circle{fill:none;stroke:var(--navy);stroke-width:1.6}
  .item-icon path{fill:none;stroke:var(--navy);stroke-width:1.6;stroke-linecap:round;stroke-linejoin:round}
  .item--mitigation{background:var(--steel);color:var(--white)}
  .item--mitigation .item-icon circle,.item--mitigation .item-icon path{stroke:var(--white)}
  .item--alert{background:var(--alert);color:var(--white)}
  .item--alert .item-icon circle,.item--alert .item-icon path{stroke:var(--white)}

  .artwork{position:absolute}
  .cover-art{left:0;top:0;width:520px;height:470px;background:radial-gradient(circle at 45% 40%,#7fa3c8 0,#a9c0d8 38%,#e6ebf1 70%)}
  .cover-band{position:absolute;left:0;top:480px;width:520px;height:110px;background:var(--navy);display:flex;align-items:center;justify-content:center;padding:0 40px}
  .cover-title{font-family:"Montserrat",Arial,sans-serif;font-weight:800;font-size:21px;line-height:1.3;color:var(--white);text-align:center;letter-spacing:.03em}
  .comms-art{left:0;top:360px;width:78px;height:250px;background:linear-gradient(180deg,#c9b3a0,#8ea7c2)}
  .banker-art{left:370px;top:40px;width:120px;height:150px;background:linear-gradient(180deg,#e3a86b,#5b7ea2)}
  .phone-art{left:390px;top:250px;width:90px;height:120px;background:linear-gradient(180deg,#f0c86a,#5b7ea2)}
  .fuel-art{left:30px;top:520px;width:130px;height:160px;background:linear-gradient(180deg,#e58a4e,#6c8fb3)}
  .map-art{left:60px;top:480px;width:430px;height:190px;background:linear-gradient(90deg,#e08a3f,#f0b55a 55%,#e6ebf1)}
  .city-art{left:0;top:500px;width:520px;height:200px;background:linear-gradient(180deg,var(--paper) 0,#b9c3cf 45%,#8a97a8 100%)}
</style>
</head>
<body>
<div class="canvas">

  <!-- Cover -->
  <section class="page page--cover">
    <div class="artwork cover-art" role="img" aria-label="Illustration of a frustrated man at a laptop with glasses pushed up"></div>
    <div class="cover-band"><h1 class="cover-title">IF EVERYTHING DIGITAL FAILS, HERE'S WHAT TO DO</h1></div>
  </section>

  <!-- Communications -->
  <section class="page page--comms">
    <div class="block" style="left:30px;top:28px;width:460px">
      <div class="section-head">
        <svg class="hex" viewBox="0 0 40 44"><polygon points="20,1 39,12 39,32 20,43 1,32 1,12"/><path d="M13 18h14M13 24h9"/></svg>
        <div><h2 class="section-title">COMMUNICATIONS</h2><p class="section-sub">If the network fails, stay in touch offline</p></div>
      </div>
    </div>
    <div class="artwork comms-art" role="img" aria-label="Illustration of a woman talking on a phone"></div>
    <div class="block" style="left:90px;top:100px;width:400px">
      <div class="item"><svg class="item-icon" viewBox="0 0 24 24"><circle cx="12" cy="12" r="11"/><path d="M8 7l2 3-1 1a6 6 0 0 0 4 4l1-1 3 2-1 2c-5 0-10-5-10-10z"/></svg><p>Phone lines and mobile data may go down without warning</p></div>
      <div class="item item--mitigation"><svg class="item-icon" viewBox="0 0 24 24"><circle cx="12" cy="12" r="11"/><path d="M7 12l3 3 7-7"/></svg><p>Keep a battery radio and agree a family meeting point</p></div>
      <div class="item"><svg class="item-icon" viewBox="0 0 24 24"><circle cx="12" cy="12" r="11"/><path d="M7 8h10v8H7zM7 8l5 4 5-4"/></svg><p>Email, chat and social apps will be unreachable for days</p></div>
      <div class="item item--mitigation"><svg class="item-icon" viewBox="0 0 24 24"><circle cx="12" cy="12" r="11"/><path d="M7 12l3 3 7-7"/></svg><p>Write key numbers on paper and store them safely</p></div>
      <div class="item"><svg class="item-icon" viewBox="0 0 24 24"><circle cx="12" cy="12" r="11"/><path d="M12 7v6M12 16v1"/></svg><p>Emergency services may be slow to respond to calls</p></div>
      <div class="item item--mitigation"><svg class="item-icon" viewBox="0 0 24 24"><circle cx="12" cy="12" r="11"/><path d="M7 12l3 3 7-7"/></svg><p>Learn local alert signals and check on neighbours</p></div>
      <div class="item"><svg class="item-icon" viewBox="0 0 24 24"><circle cx="12" cy="12" r="11"/><path d="M8 7h8v10H8zM10 10h4M10 13h4"/></svg><p>Public notices may return to print and posters</p></div>
    </div>
  </section>

  <!-- Banking & Transportation -->
  <section class="page page--banking">
    <div class="block" style="left:30px;top:30px;width:330px">
      <div class="section-head">
        <svg class="hex" viewBox="0 0 40 44"><polygon points="20,1 39,12 39,32 20,43 1,32 1,12"/><path d="M12 29h16M14 19v8M20 19v8M26 19v8M11 17l9-5 9 5"/></svg>
        <div><h2 class="section-title">BANKING</h2><p class="section-sub">Card payments and online accounts may stop</p></div>
      </div>
      <div class="item"><svg class="item-icon" viewBox="0 0 24 24"><circle cx="12" cy="12" r="11"/><path d="M6 9h12v7H6zM6 12h12"/></svg><p>Cash machines and card readers need a live network</p></div>
      <div class="item item--mitigation"><svg class="item-icon" viewBox="0 0 24 24"><circle cx="12" cy="12" r="11"/><path d="M7 12l3 3 7-7"/></svg><p>Keep a small cash reserve at home</p></div>
    </div>
    <div class="artwork banker-art" role="img" aria-label="Illustration of a bearded man with a cash card"></div>

    <div class="block" style="left:30px;top:250px;width:340px">
      <div class="section-head">
        <svg class="hex" viewBox="0 0 40 44"><polygon points="20,1 39,12 39,32 20,43 1,32 1,12"/><path d="M12 29h16M14 19v8M20 19v8M26 19v8M11 17l9-5 9 5"/></svg>
        <div><h2 class="section-title">BANKING</h2><p class="section-sub">Plan for bills and transfers while offline</p></div>
      </div>
      <div class="item"><svg class="item-icon" viewBox="0 0 24 24"><circle cx="12" cy="12" r="11"/><path d="M8 7h8v10H8zM10 10h4M10 13h4"/></svg><p>Keep paper statements and a list of account numbers</p></div>
    </div>
    <div class="artwork phone-art" role="img" aria-label="Illustration of a hand holding a smartphone with coins"></div>

    <div class="block" style="left:180px;top:440px;width:310px">
      <div class="section-head">
        <svg class="hex" viewBox="0 0 40 44"><polygon points="20,1 39,12 39,32 20,43 1,32 1,12"/><path d="M12 26h16M13 26l2-6h10l2 6M15 29v1M25 29v1"/></svg>
        <div><h2 class="section-title">TRANSPORTATION</h2><p class="section-sub">Fuel, tickets and navigation need planning</p></div>
      </div>
      <div class="item"><svg class="item-icon" viewBox="0 0 24 24"><circle cx="12" cy="12" r="11"/><path d="M8 17V7h6v10M14 10h2v5"/></svg><p>Fuel pumps and ticket gates may be offline</p></div>
      <div class="item item--mitigation"><svg class="item-icon" viewBox="0 0 24 24"><circle cx="12" cy="12" r="11"/><path d="M7 12l3 3 7-7"/></svg><p>Keep a paper map and a half full tank</p></div>
    </div>
    <div class="artwork fuel-art" role="img" aria-label="Illustration of a fuel pump and an attendant"></div>
  </section>

  <!-- Information management -->
  <section class="page page--info">
    <div class="block" style="left:30px;top:30px;width:460px">
      <div class="section-head">
        <svg class="hex" viewBox="0 0 40 44"><polygon points="20,1 39,12 39,32 20,43 1,32 1,12"/><path d="M13 15h14v14H13zM16 20h8M16 24h8"/></svg>
        <div><h2 class="section-title">INFORMATION MANAGEMENT</h2><p class="section-sub">Protect records you rely on every day</p></div>
      </div>
      <div class="item"><svg class="item-icon" viewBox="0 0 24 24"><circle cx="12" cy="12" r="11"/><path d="M7 15a3 3 0 0 1 1-6 4 4 0 0 1 8 1 3 3 0 0 1 0 5z"/></svg><p>Cloud files and online records may be unreachable</p></div>
      <div class="item item--alert" style="padding:16px 12px"><svg class="item-icon" viewBox="0 0 24 24"><circle cx="12" cy="12" r="11"/><path d="M12 7v6M12 16v1"/></svg><p>Print key documents: IDs, insurance, prescriptions and contacts</p></div>
      <div class="item item--mitigation"><svg class="item-icon" viewBox="0 0 24 24"><circle cx="12" cy="12" r="11"/><path d="M7 12l3 3 7-7"/></svg><p>Store copies in a dry folder</p></div>
    </div>

    <div class="block" style="left:30px;top:290px;width:460px">
      <div class="section-head">
        <svg class="hex" viewBox="0 0 40 44"><polygon points="20,1 39,12 39,32 20,43 1,32 1,12"/><path d="M13 15h14v14H13zM16 20h8M16 24h8"/></svg>
        <div><h2 class="section-title">INFORMATION MANAGEMENT</h2><p class="section-sub">Share trusted information with people nearby</p></div>
      </div>
      <div class="item"><svg class="item-icon" viewBox="0 0 24 24"><circle cx="12" cy="12" r="11"/><path d="M7 9h10v6h-6l-3 2v-2H7z"/></svg><p>Rumours spread fast when news sites go dark</p></div>
      <div class="item item--mitigation"><svg class="item-icon" viewBox="0 0 24 24"><circle cx="12" cy="12" r="11"/><path d="M7 12l3 3 7-7"/></svg><p>Use one trusted local source</p></div>
    </div>
    <div class="artwork map-art" role="img" aria-label="Illustration of a man beside a world map with connected people"></div>
  </section>

  <!-- Technology -->
  <section class="page page--tech">
    <div class="block" style="left:30px;top:30px;width:460px">
      <div class="section-head">
        <svg class="hex" viewBox="0 0 40 44"><polygon points="20,1 39,12 39,32 20,43 1,32 1,12"/><path d="M13 16h14v10H13zM17 29h6"/></svg>
        <div><h2 class="section-title">TECHNOLOGY</h2><p class="section-sub">Keep devices useful without a connection</p></div>
      </div>
      <div class="item"><svg class="item-icon" viewBox="0 0 24 24"><circle cx="12" cy="12" r="11"/><path d="M12 7v8M9 12l3 3 3-3M8 17h8"/></svg><p>Download offline maps, manuals and guides in advance</p></div>
      <div class="item"><svg class="item-icon" viewBox="0 0 24 24"><circle cx="12" cy="12" r="11"/><path d="M7 9h9v6H7zM16 11h1v2"/></svg><p>Charge power banks and keep spare batteries</p></div>
      <div class="item item--alert" style="padding:16px 12px"><svg class="item-icon" viewBox="0 0 24 24"><circle cx="12" cy="12" r="11"/><path d="M12 7v6M12 16v1"/></svg><p>Do not plug in unknown drives or devices</p></div>
      <div class="item item--mitigation"><svg class="item-icon" viewBox="0 0 24 24"><circle cx="12" cy="12" r="11"/><path d="M7 12l3 3 7-7"/></svg><p>Keep a solar charger ready</p></div>
    </div>

    <div class="block" style="left:30px;top:450px;width:460px">
      <div class="section-head">
        <svg class="hex" viewBox="0 0 40 44"><polygon points="20,1 39,12 39,32 20,43 1,32 1,12"/><path d="M13 16h14v10H13zM17 29h6"/></svg>
        <div><h2 class="section-title">TECHNOLOGY</h2><p class="section-sub">Recover calmly once service returns</p></div>
      </div>
      <div class="item"><svg class="item-icon" viewBox="0 0 24 24"><circle cx="12" cy="12" r="11"/><path d="M8 11h8v6H8zM10 11V9a2 2 0 0 1 4 0v2"/></svg><p>Update passwords and check accounts for changes</p></div>
      <div class="item item--mitigation"><svg class="item-icon" viewBox="0 0 24 24"><circle cx="12" cy="12" r="11"/><path d="M7 12l3 3 7-7"/></svg><p>Restore from your own backups first</p></div>
    </div>
  </section>

  <!-- Closing page -->
  <section class="page page--closing">
    <div class="artwork city-art" role="img" aria-label="Illustration of a small town skyline with mountains and a hot air balloon"></div>
  </section>

</div>
</body>
</html>
```